Book cover for a book about how to support a friend in grief.

The title of the book is "Quiet Hands on Heavy Days: Standing Beside Someone Across Hard Seasons" by Daniel P. Hartwig. I am a grief counselor and am passionate about educating people on how to better support someone in grief. I'd like the cover to tell a story. Maybe a person in grief and a friend standing near who doesn't know what to say. The image should appeal to all genders. I am open to ANY other ideas for the cover. Grief is a heavy topic but I don't want the cover to feel sad. It should convey hope.

```html
<!DOCTYPE html>
<html lang="en">
<head>
<meta charset="utf-8">
<title>Quiet Hands on Heavy Days — Book Cover</title>
<link rel="stylesheet" href="https://fonts.googleapis.com/css2?family=Cabin:wght@700&family=EB+Garamond&family=Yellowtail&display=swap">
<style>
  :root {
    --cover-green: #00a651;
    --cover-green-light: #93cf80;
    --ink-black: #0c0c0c;
    --paper-white: #ffffff;
    --glow-lime: #c6f25a;
    --ground-brown: #4e4343;
  }
  * { margin: 0; padding: 0; box-sizing: border-box; }
  html, body {
    width: 1200px; height: 848px; overflow: hidden;
    background: var(--cover-green);
  }
  .cover-wrap {
    position: relative;
    width: 1200px; height: 848px;
    background: linear-gradient(to bottom,
      var(--cover-green) 0%, var(--cover-green) 93%, var(--cover-green-light) 100%);
    overflow: hidden;
  }
  .author-script {
    font-family: "Yellowtail", cursive;
    color: var(--ink-black);
    white-space: nowrap;
  }

  /* Back cover */
  .back-author {
    position: absolute; left: 308px; top: 340px;
    transform: translateX(-50%);
    font-size: 27px;
  }
  .back-blurb {
    position: absolute; left: 308px; top: 386px;
    transform: translateX(-50%);
    width: 400px;
    font-family: "EB Garamond", serif;
    font-size: 16.5px; line-height: 28px;
    color: var(--paper-white);
    text-align: center;
  }

  /* Spine */
  .spine-author {
    position: absolute; left: 601px; top: 114px;
    transform: translate(-50%, -50%) rotate(90deg);
    font-size: 19px;
  }
  .spine-title {
    position: absolute; left: 601px; top: 560px;
    transform: translate(-50%, -50%) rotate(-90deg);
    font-family: "Cabin", sans-serif; font-weight: 700;
    font-size: 16px; line-height: 19px;
    color: var(--paper-white);
    white-space: nowrap;
  }

  /* Front cover */
  .front-author {
    position: absolute; left: 884px; top: 86px;
    transform: translateX(-50%);
    font-size: 29px;
  }
  .front-title {
    position: absolute; left: 886px; top: 168px;
    transform: translateX(-50%);
    font-family: "Cabin", sans-serif; font-weight: 700;
    font-size: 38px; line-height: 48px;
    color: var(--paper-white);
    text-align: center;
    white-space: nowrap;
    text-shadow: 0 0 4px var(--glow-lime), 0 0 8px var(--glow-lime), 0 0 12px rgba(198,242,90,.7);
  }
  .front-scene {
    position: absolute; left: 621px; top: 549px;
    width: 539px; height: 259px;
  }
</style>
</head>
<body>
  <main class="cover-wrap">
    <section class="back-cover">
      <p class="author-script back-author">Daniel P. Hartwig</p>
      <p class="back-blurb">I am a grief counselor and am passionate about educating people on how to better support someone in grief</p>
    </section>

    <section class="spine">
      <p class="author-script spine-author">Daniel P. Hartwig</p>
      <h2 class="spine-title">Quiet Hands on Heavy Days:<br>Standing Beside Someone Across Hard Seasons</h2>
    </section>

    <section class="front-cover">
      <p class="author-script front-author">Daniel P. Hartwig</p>
      <h1 class="front-title">Quiet Hands<br>on Heavy Days:<br>Standing Beside<br>Someone Across<br>Hard Seasons</h1>
      <svg class="front-scene" viewBox="0 0 539 259" role="img"
           aria-label="Silhouette scene: a grieving person seated on a bench, head in hand, with a friend standing nearby on dark ground">
        <defs>
          <linearGradient id="scene-fade" x1="0" y1="0" x2="0" y2="1">
            <stop offset="0" stop-color="#00a651"/>
            <stop offset="0.55" stop-color="#4e4343" stop-opacity="0.85"/>
            <stop offset="0.66" stop-color="#4e4343"/>
            <stop offset="1" stop-color="#4e4343"/>
          </linearGradient>
        </defs>
        <rect width="539" height="259" fill="url(#scene-fade)"/>
      </svg>
    </section>
  </main>
</body>
</html>
```